Tidewell Provisions

Distributor of seasonings and spices to the restaurant industry.

Restaurant

Tidewell Provis
Dean Holcroft
TK Wandsley Distributor
317-640-8917
dean@tidewellprovisionsco.com

No minimum order
Gluten & MSG free soup bases

```html
<!DOCTYPE html>
<html lang="en">
<head>
<meta charset="utf-8">
<title>Tidewell Provisions – Business Card</title>
<link rel="stylesheet" href="https://fonts.googleapis.com/css2?family=Open+Sans:wght@400;600;700&display=swap">
<style>
  :root {
    --backdrop: #e9e5df;
    --card-white: #ffffff;
    --pepper-red: #e8231c;
    --pepper-red-deep: #d41a14;
    --roast-brown: #3b2a26;
    --saffron: #f2c53d;
    --text-light: #ffffff;
  }
  * { box-sizing: border-box; margin: 0; padding: 0; }
  html, body {
    width: 1200px;
    height: 950px;
    overflow: hidden;
    background: var(--backdrop);
    font-family: "Open Sans", Arial, sans-serif;
  }
  .business-card {
    position: absolute;
    left: 150px;
    top: 218px;
    width: 900px;
    height: 514px;
    border-radius: 34px;
    overflow: hidden;
    background: var(--card-white);
    box-shadow: 0 12px 34px rgba(0,0,0,0.18);
  }
  .card-art {
    position: absolute;
    inset: 0;
    width: 900px;
    height: 514px;
  }
  .brand-lockup {
    position: absolute;
    left: 520px;
    top: 140px;
    display: flex;
    align-items: center;
    gap: 16px;
  }
  .brand-mark {
    width: 46px;
    height: 46px;
    border-radius: 50%;
    background: var(--saffron);
  }
  .brand-name {
    font-size: 34px;
    font-weight: 600;
    color: var(--roast-brown);
    letter-spacing: 0.5px;
  }
  .contact-block {
    position: absolute;
    left: 44px;
    top: 328px;
    color: var(--text-light);
  }
  .contact-name {
    font-size: 25px;
    font-weight: 700;
    margin-bottom: 2px;
  }
  .contact-title {
    font-size: 15px;
    font-weight: 400;
    margin-bottom: 16px;
  }
  .contact-line {
    display: flex;
    align-items: center;
    gap: 12px;
    font-size: 15px;
    line-height: 26px;
  }
  .contact-icon {
    width: 15px;
    height: 15px;
    flex: none;
  }
</style>
</head>
<body>
  <article class="business-card">
    <svg class="card-art" viewBox="0 0 900 514" aria-hidden="false">
      <path class="red-panel" role="img" aria-label="Red panel with tone-on-tone damask pattern"
            d="M0,300 C220,255 340,470 610,468 C750,466 850,425 900,400 L900,514 L0,514 Z"
            fill="var(--pepper-red)"/>
      <path class="stripe-brown" d="M0,292 C220,246 340,460 610,458 C750,456 850,415 900,390"
            fill="none" stroke="var(--roast-brown)" stroke-width="12"/>
      <path class="stripe-saffron" d="M0,280 C220,234 340,446 610,444 C750,442 850,401 900,376"
            fill="none" stroke="var(--saffron)" stroke-width="7"/>
    </svg>

    <div class="brand-lockup">
      <span class="brand-mark"></span>
      <span class="brand-name">Tidewell Provisions</span>
    </div>

    <div class="contact-block">
      <p class="contact-name">Dean Holcroft</p>
      <p class="contact-title">TK Wandsley Distributor</p>
      <p class="contact-line">
        <svg class="contact-icon" viewBox="0 0 16 16"><path d="M3 1h3l1.5 4-2 1.2a9 9 0 0 0 4.3 4.3L11 8.5l4 1.5v3a2 2 0 0 1-2 2A12 12 0 0 1 1 3a2 2 0 0 1 2-2z" fill="#fff"/></svg>
        317-640-8917
      </p>
      <p class="contact-line">
        <svg class="contact-icon" viewBox="0 0 16 16"><rect x="1" y="3" width="14" height="10" rx="1" fill="#fff"/><path d="M1.5 3.5 8 9l6.5-5.5" fill="none" stroke="var(--pepper-red)" stroke-width="1.4"/></svg>
        dean@tidewellprovisionsco.com
      </p>
      <p class="contact-line">
        <svg class="contact-icon" viewBox="0 0 16 16"><circle cx="8" cy="8" r="7" fill="none" stroke="#fff" stroke-width="1.5"/><ellipse cx="8" cy="8" rx="3" ry="7" fill="none" stroke="#fff" stroke-width="1.2"/><path d="M1 8h14" stroke="#fff" stroke-width="1.2"/></svg>
        www.tidewellprovisionsco.com
      </p>
    </div>
  </article>
</body>
</html>
```